Bus Bench Ad Design Needed

Hi there. We would like to design an eye catching bus bench ad! The information that we would like to have on it is found below:

- Our logo which is attached below. We would this to take up at least half of the bus bench.
- Our phone number in bold, very visible to see. 813-562-0947. White numbers on an eye catching colored background.
- Our web address : www.SplitEase247.example
- A "Ring Gary" phrase in a black circle with yellow bold letters. Want the "Ring Gary" to be somewhat angled. We are thinking that the "Ring Gary" should be directly below the image in our logo.
- Our tag line we want somewhere in here as well which is "Divorce made easy - at a price you'll like!"

```html
<!DOCTYPE html>
<html lang="en">
<head>
<meta charset="utf-8">
<title>SplitEase Bus Bench Ad</title>
<link rel="stylesheet" href="https://fonts.googleapis.com/css2?family=Roboto+Condensed:wght@700&family=Poppins:ital,wght@1,800&family=Montserrat:wght@500&display=swap">
<style>
  :root {
    --brand-blue: #1b82c5;
    --ink: #0d0d0d;
    --paper: #ffffff;
    --stage: #e6e6e6;
    --text-dark: #1f1f1f;
    --accent-yellow: #ffd21f;
    --photo-top: #474d55;
    --photo-bottom: #d9b48c;
  }
  * { margin: 0; padding: 0; box-sizing: border-box; }
  html, body {
    width: 1200px; height: 862px; overflow: hidden;
    background: var(--stage);
  }
  .bench-ad {
    position: absolute; left: 30px; top: 268px;
    width: 1140px; height: 325px;
    background: var(--paper);
    overflow: hidden;
  }
  .bench-ad__shapes { position: absolute; inset: 0; }
  .hero-photo {
    position: absolute; left: 0; top: 0; width: 520px; height: 230px;
    clip-path: polygon(0 0, 384px 0, 520px 230px, 0 230px);
    background: linear-gradient(180deg, var(--photo-top) 0%, var(--photo-bottom) 100%);
  }
  .call-bubble {
    position: absolute; left: 36px; top: 76px; width: 144px; height: 144px;
    border-radius: 50%;
    background: var(--ink);
    transform: rotate(-10deg);
    display: flex; flex-direction: column; align-items: center; justify-content: center;
    font-family: "Roboto Condensed", sans-serif; font-weight: 700;
    color: var(--accent-yellow); line-height: 1.05;
  }
  .call-bubble__verb { font-size: 40px; }
  .call-bubble__name { font-size: 42px; }
  .brand {
    position: absolute; left: 540px; top: 36px;
    display: flex; align-items: center; gap: 22px;
  }
  .brand__mark {
    width: 78px; height: 78px; border-radius: 50%;
    background: var(--brand-blue);
  }
  .brand__divider { width: 2px; height: 96px; background: #9a9a9a; }
  .brand__name {
    font-family: "Montserrat", sans-serif; font-weight: 500;
    font-size: 68px; color: var(--brand-blue); letter-spacing: 1px; line-height: 1;
  }
  .brand__sub {
    font-family: "Montserrat", sans-serif; font-weight: 500;
    font-size: 24px; color: var(--text-dark); margin-top: 6px; white-space: nowrap;
  }
  .tagline {
    position: absolute; left: 540px; top: 186px; height: 40px;
    display: flex; align-items: center;
    font-family: "Roboto Condensed", sans-serif; font-weight: 700;
    font-size: 26px; letter-spacing: 0.3px; white-space: nowrap;
  }
  .tagline__lead { color: var(--paper); }
  .tagline__tail { color: var(--ink); }
  .phone {
    position: absolute; left: 42px; top: 234px; height: 91px;
    display: flex; align-items: center;
    font-family: "Poppins", sans-serif; font-style: italic; font-weight: 800;
    font-size: 74px; color: var(--paper); letter-spacing: -1px;
  }
  .web {
    position: absolute; left: 686px; top: 234px; height: 91px;
    display: flex; align-items: center;
    font-family: "Roboto Condensed", sans-serif; font-weight: 700;
    font-size: 27px; color: var(--brand-blue); letter-spacing: 0.5px;
  }
</style>
</head>
<body>
  <div class="bench-ad">
    <div class="hero-photo" role="img" aria-label="Photo of a person in a suit signing papers at a desk beside a wooden gavel"></div>
    <svg class="bench-ad__shapes" width="1140" height="325" viewBox="0 0 1140 325" aria-hidden="true">
      <polygon points="492,182 1140,182 1140,228 519,228" fill="var(--brand-blue)"/>
      <polygon points="0,232 606,232 665,325 0,325" fill="var(--brand-blue)"/>
      <polygon points="606,232 1140,232 1140,325 665,325" fill="var(--ink)"/>
    </svg>
    <div class="call-bubble">
      <span class="call-bubble__verb">Ring</span>
      <span class="call-bubble__name">GARY</span>
    </div>
    <div class="brand">
      <div class="brand__mark"></div>
      <div class="brand__divider"></div>
      <div class="brand__text">
        <div class="brand__name">SplitEase</div>
        <div class="brand__sub">Non-Lawyer Documents Service</div>
      </div>
    </div>
    <div class="tagline">
      <span class="tagline__lead">DIVORCE MADE EASY&nbsp;</span><span class="tagline__tail">- AT A PRICE YOU'LL LIKE!</span>
    </div>
    <div class="phone">813-562-0947</div>
    <div class="web">WWW.SPLITEASE247.EXAMPLE</div>
  </div>
</body>
</html>
```